Quiet Harbor Counseling Business Card design with a visually interesting use of Space

I need business cards that are luxurious and give a peaceful, calm vibe. I also had some letterhead designed, and i like the look of it also, it's attached with the logo design for reference/ ideas but feel free to be creative.

Target Market(s)

High end luxurious client who needs counseling

Industry/Entity Type

Marriage and Family Therapy

Contact Information for Business Card

Corra Mabbitt MS LMFT/ or Tobin Walsh address 4175 Pemberly Suite 620

Font styles to use
Sans Serif

Colors
0054AA
0677BA
7BADD7
CADEEF
E8F1F8
0094D4
00A9DD
6FCCEA
C7EBF8
E9F6FB
A7469A
B969AE
D3A5CF
EDDBEB
F8F0F9
6B429C
8869AF
B7A5CE
E3DAEB
F3F0F8

Requirements
Must have
• Logo and color scheme but be simple modern and luxurious
Nice to have
• I'd like to incorporate some elelmets from the logo and letterhead into a simple modern card

```html
<!DOCTYPE html>
<html lang="en">
<head>
<meta charset="utf-8">
<title>Quiet Harbor Counseling – Business Card</title>
<link rel="stylesheet" href="https://fonts.googleapis.com/css2?family=Montserrat:wght@400;500&family=Jost:wght@300&display=swap">
<style>
  :root {
    --backdrop: #ababab;
    --card-white: #ffffff;
    --plum: #a7469a;
    --violet: #6b429c;
    --text-grey: #7a7a7a;
    --night-deep: #0c0a33;
    --night-indigo: #251a6e;
    --night-violet: #4a1d6e;
    --wordmark-light: #f3f0f8;
    --orb: #8869af;
  }
  * { margin: 0; padding: 0; box-sizing: border-box; }
  html, body { width: 1200px; height: 1000px; overflow: hidden; }
  body {
    background: var(--backdrop);
    position: relative;
    font-family: "Montserrat", sans-serif;
  }
  .card {
    position: absolute;
    width: 612px;
    height: 355px;
    overflow: hidden;
  }
  .card--front {
    left: 295px; top: 113px;
    background: var(--card-white);
    border-radius: 45px 45px 0 45px;
  }
  .card--back {
    left: 296px; top: 531px;
    border-radius: 45px 45px 0 45px;
  }
  .brand-front {
    position: absolute;
    left: 62px; top: 92px;
    width: 220px;
    display: flex;
    align-items: center;
    gap: 14px;
  }
  .brand-front__dot {
    flex: none;
    width: 44px; height: 44px;
    border-radius: 50%;
    background: var(--orb);
    opacity: .85;
  }
  .brand-front__name {
    font-family: "Montserrat", sans-serif;
    font-weight: 400;
    font-size: 21px;
    line-height: 1.25;
    color: var(--plum);
  }
  .contact {
    position: absolute;
    left: 308px; top: 100px;
    color: var(--text-grey);
    font-size: 15.5px;
    line-height: 19px;
  }
  .contact__name {
    color: var(--plum);
    font-size: 23px;
    font-weight: 400;
    letter-spacing: .3px;
    margin-bottom: 14px;
  }
  .contact__address { margin-top: 38px; }
  .contact__web {
    margin-top: 18px;
    color: var(--plum);
    font-weight: 500;
    font-size: 16px;
  }
  .night-sky {
    position: absolute; inset: 0;
    background:
      radial-gradient(ellipse at 30% 20%, var(--night-indigo) 0%, transparent 60%),
      radial-gradient(ellipse at 85% 80%, var(--night-violet) 0%, transparent 65%),
      linear-gradient(120deg, var(--night-deep) 0%, var(--night-indigo) 45%, var(--night-violet) 100%);
  }
  .brand-back {
    position: absolute;
    left: 150px; top: 110px;
    display: flex;
    align-items: flex-start;
    gap: 8px;
    color: var(--wordmark-light);
    font-family: "Jost", sans-serif;
    font-weight: 300;
  }
  .brand-back__text { text-align: right; }
  .brand-back__title { font-size: 44px; line-height: 1.1; }
  .brand-back__sub { font-size: 20px; letter-spacing: 2.5px; margin-top: 2px; }
  .brand-back__dot {
    width: 56px; height: 56px;
    border-radius: 50%;
    background: var(--orb);
    opacity: .8;
    margin-top: -12px;
  }
</style>
</head>
<body>
  <section class="card card--front">
    <div class="brand-front">
      <span class="brand-front__dot"></span>
      <span class="brand-front__name">Quiet Harbor Counseling</span>
    </div>
    <div class="contact">
      <p class="contact__name">Tobin Walsh</p>
      <p class="contact__phone">214.555.0148</p>
      <p class="contact__email">tobin@quietharborcounseling.com</p>
      <p class="contact__address">4175 Pemberly Suite 620<br>Dallas, TX 75206</p>
      <p class="contact__web">quietharborcounseling.com</p>
    </div>
  </section>

  <section class="card card--back">
    <div class="night-sky" role="img" aria-label="Starry violet night sky background"></div>
    <div class="brand-back">
      <div class="brand-back__text">
        <p class="brand-back__title">Quiet Harbor</p>
        <p class="brand-back__sub">Counseling</p>
      </div>
      <span class="brand-back__dot"></span>
    </div>
  </section>
</body>
</html>
```